Brochure for Law Support Services Company

Hi
I need a 2-fold brochure for my small company. We provide office services for law firms in Brazil. The company website is this one: www.vtamplexo.com.br
A law firm can have an internal admin team that does all bureaucratic/official work at tribunals.  These services range from lawsuits copies, certification, registrar and we also perform official duties like representing law firms in judgements. It is costly for customers to do this in-house as they lack scale and expertise.
My company offer outsource this services, with the following advantages:
1) We offer countrywide coverage
2) Customers can order and follow their service online
3) We have agreed pre-defined prices
4) We guarantee timeliness and accuracy
We achieve this thru 3 pillars: expertise, process and technology.
I need a brochure that has some basic sessions, describing our services, how we work and the value we provide. You dont need to write in Portuguese, but I need the structure so I can fill the gaps with text.
For example, I need a Brazilian map showing our coverage, the 3 pillars, an area for a case study, a session that shows our value prop.
Thanks
Nelo

Target Market(s)
Law firms
Industry/Entity Type
Law Firm
Requirements
Must have
- Professional - example attached
Logo attached
If someone make me one like the one I attached it will have higher chance to win (instead of Australia map) I need a brazilian on the same look/feel
Should not have
- Casual look

```html
<!DOCTYPE html>
<html lang="en">
<head>
<meta charset="utf-8">
<title>Law Support Services – Brochure Inside Spread</title>
<link href="https://fonts.googleapis.com/css2?family=Barlow:wght@400;600&display=swap" rel="stylesheet">
<style>
  :root {
    --page-bg: #e7e4e0;
    --panel-grey: #c8c9c9;
    --panel-light: #eeeeee;
    --plum: #84264f;
    --slate: #666766;
    --ink: #2b2b2b;
    --white: #ffffff;
  }
  * { box-sizing: border-box; margin: 0; padding: 0; }
  html, body {
    width: 1200px;
    height: 800px;
    overflow: hidden;
    background: var(--page-bg);
  }
  .brochure {
    position: absolute;
    left: 68px;
    top: 24px;
    width: 1064px;
    height: 752px;
    display: grid;
    grid-template-columns: repeat(7, 1fr);
    box-shadow: 0 6px 18px rgba(0,0,0,0.18);
    font-family: "Barlow", sans-serif;
    color: var(--ink);
  }
  .panel { display: flex; flex-direction: column; height: 100%; overflow: hidden; }
  .panel--grey { background: var(--panel-grey); }
  .panel--light { background: var(--panel-light); }
  .panel-body { height: 543px; padding: 19px 17px 0 19px; }

  .section-title {
    font-size: 12px;
    line-height: 14px;
    font-weight: 600;
    color: var(--plum);
    text-transform: uppercase;
    letter-spacing: 0.04em;
    padding-bottom: 6px;
    margin-bottom: 8px;
    border-bottom: 1px solid var(--plum);
  }
  .copy {
    font-size: 7.6px;
    line-height: 9.5px;
    text-align: justify;
  }
  .copy + .copy { margin-top: 7px; }
  .sub-title {
    font-size: 8.4px;
    line-height: 10px;
    font-weight: 600;
    color: var(--plum);
    margin: 10px 0 3px;
  }

  .service-list, .value-list { list-style: none; margin-top: 8px; }
  .service-list li {
    font-size: 7.6px;
    line-height: 9.5px;
    padding: 5px 0 5px 10px;
    border-bottom: 1px solid rgba(0,0,0,0.15);
    position: relative;
  }
  .service-list li::before {
    content: "";
    position: absolute;
    left: 0; top: 8px;
    width: 5px; height: 5px;
    background: var(--plum);
  }
  .service-list strong { display: block; font-weight: 600; }

  .step {
    background: var(--white);
    border-left: 3px solid var(--plum);
    padding: 6px 7px;
    font-size: 7.6px;
    line-height: 9.5px;
  }
  .step strong { display: block; font-weight: 600; color: var(--plum); }
  .step-arrow { display: block; margin: 3px auto; }

  .map-area {
    height: 200px;
    margin: 4px 0 8px;
    background: radial-gradient(ellipse at 55% 45%, #9c4a6d 0%, #84264f 55%, #b9a0ab 100%);
  }
  .stat-row { display: flex; gap: 6px; margin-top: 10px; }
  .stat {
    flex: 1;
    background: var(--plum);
    color: var(--white);
    text-align: center;
    padding: 7px 2px;
  }
  .stat b { display: block; font-size: 15px; line-height: 16px; font-weight: 600; }
  .stat span { font-size: 7px; line-height: 8px; }

  .pillar { display: flex; gap: 8px; align-items: flex-start; margin-top: 12px; }
  .pillar-mark {
    flex: 0 0 22px; height: 22px; border-radius: 50%;
    background: var(--plum); color: var(--white);
    font-size: 10px; font-weight: 600; line-height: 22px; text-align: center;
  }
  .pillar-text { font-size: 7.6px; line-height: 9.5px; text-align: justify; }
  .pillar-text strong { display: block; font-size: 8.4px; font-weight: 600; color: var(--plum); margin-bottom: 2px; }

  .case-label { font-size: 7.6px; font-weight: 600; color: var(--plum); text-transform: uppercase; letter-spacing: 0.04em; margin: 9px 0 2px; }
  .chart { margin-top: 8px; display: block; }

  .value-list li {
    display: flex; gap: 6px;
    font-size: 7.6px; line-height: 9.5px;
    padding: 6px 0;
    border-bottom: 1px solid rgba(0,0,0,0.15);
  }
  .value-list svg { flex: 0 0 10px; margin-top: 0; }
  .value-list strong { display: block; font-weight: 600; }
  .contact {
    margin-top: 12px;
    background: var(--plum);
    color: var(--white);
    padding: 8px;
    font-size: 7.6px;
    line-height: 10px;
  }
  .contact strong { display: block; font-size: 8.4px; font-weight: 600; }

  .photo { flex: 1; width: 100%; }
  .photo--handshake { background: linear-gradient(160deg, #d9c4b4 0%, #b78f76 45%, #5b4a42 100%); }
  .photo--signing { background: linear-gradient(150deg, #f4f2ef 0%, #d6cfc8 50%, #8c8178 100%); }
  .photo--office { background: linear-gradient(140deg, #efe8e0 0%, #b89a86 45%, #2f3038 100%); }
  .photo--meeting { background: linear-gradient(170deg, #e8e8ea 0%, #b6b8bd 50%, #4a4f5a 100%); }
  .photo--teamwork { background: linear-gradient(160deg, #9aa0a8 0%, #c79f86 50%, #5a4c48 100%); }
  .photo--review { background: linear-gradient(150deg, #f1eeeb 0%, #d9b9a5 55%, #7c8aa0 100%); }

  .spine { display: flex; flex-direction: column; height: 100%; }
  .spine-band { flex: 0 0 674px; background: var(--plum); }
  .spine-foot { flex: 1; background: var(--slate); }
</style>
</head>
<body>
<main class="brochure">

  <section class="panel panel--grey">
    <div class="panel-body">
      <h2 class="section-title">Our Services</h2>
      <p class="copy">We take care of the bureaucratic and official work that law firms need at tribunals, so your team can focus on the law. Insert a short introduction to the company here.</p>
      <ul class="service-list">
        <li><strong>Lawsuit copies</strong>Short description of the service and its scope.</li>
        <li><strong>Certification</strong>Short description of the service and its scope.</li>
        <li><strong>Registrar filings</strong>Short description of the service and its scope.</li>
        <li><strong>Representation at judgements</strong>Short description of the service and its scope.</li>
        <li><strong>Official duties</strong>Short description of the service and its scope.</li>
      </ul>
      <h3 class="sub-title">Why outsource?</h3>
      <p class="copy">Keeping an in-house admin team is costly for law firms that lack scale and expertise. Add a few lines here on the savings a firm can expect.</p>
    </div>
    <div class="photo photo--handshake" role="img" aria-label="Photo of two business people shaking hands over a desk with a pen"></div>
  </section>

  <section class="panel panel--light">
    <div class="panel-body">
      <h2 class="section-title">How We Work</h2>
      <p class="copy">A simple process from order to delivery. Add a sentence on the workflow here.</p>
      <div style="margin-top:10px">
        <div class="step"><strong>1. Order online</strong>Place the request on our portal in a few clicks.</div>
        <svg class="step-arrow" width="10" height="8" viewBox="0 0 10 8"><path d="M0 0h10L5 8z" fill="#84264f"/></svg>
        <div class="step"><strong>2. Local assignment</strong>A team near the tribunal takes over the task.</div>
        <svg class="step-arrow" width="10" height="8" viewBox="0 0 10 8"><path d="M0 0h10L5 8z" fill="#84264f"/></svg>
        <div class="step"><strong>3. Follow online</strong>Track each stage of the service in real time.</div>
        <svg class="step-arrow" width="10" height="8" viewBox="0 0 10 8"><path d="M0 0h10L5 8z" fill="#84264f"/></svg>
        <div class="step"><strong>4. Delivery</strong>Receive the result on time at the agreed price.</div>
      </div>
      <h3 class="sub-title">Service levels</h3>
      <p class="copy">Describe agreed deadlines, reporting and quality checks here.</p>
    </div>
    <div class="photo photo--signing" role="img" aria-label="Photo of hands signing documents beside a coffee cup"></div>
  </section>

  <section class="panel panel--grey">
    <div class="panel-body">
      <h2 class="section-title">Coverage</h2>
      <p class="copy">We serve tribunals in every state of Brazil.</p>
      <div class="map-area" role="img" aria-label="Map of Brazil in plum tones with the covered states marked"></div>
      <p class="copy">Add a short text about the network of partners and offices that gives countrywide reach.</p>
      <div class="stat-row">
        <div class="stat"><b>27</b><span>states</span></div>
        <div class="stat"><b>00</b><span>cities</span></div>
      </div>
      <div class="stat-row">
        <div class="stat"><b>00</b><span>tribunals</span></div>
        <div class="stat"><b>00</b><span>orders / year</span></div>
      </div>
    </div>
    <div class="photo photo--office" role="img" aria-label="Photo of a smiling businesswoman shaking hands with a client in an office"></div>
  </section>

  <section class="spine" aria-hidden="true">
    <div class="spine-band"></div>
    <div class="spine-foot"></div>
  </section>

  <section class="panel panel--grey">
    <div class="panel-body">
      <h2 class="section-title">Our 3 Pillars</h2>
      <p class="copy">Our results rest on three pillars that work together.</p>
      <div class="pillar">
        <div class="pillar-mark">1</div>
        <p class="pillar-text"><strong>Expertise</strong>Describe the team’s legal and tribunal experience and how it reduces errors for clients.</p>
      </div>
      <div class="pillar">
        <div class="pillar-mark">2</div>
        <p class="pillar-text"><strong>Process</strong>Describe the standard procedures and checks that make every order predictable.</p>
      </div>
      <div class="pillar">
        <div class="pillar-mark">3</div>
        <p class="pillar-text"><strong>Technology</strong>Describe the online platform used to order, follow and store every service.</p>
      </div>
      <h3 class="sub-title">Working together</h3>
      <p class="copy">Add a closing line on how the pillars combine to deliver timeliness and accuracy.</p>
    </div>
    <div class="photo photo--meeting" role="img" aria-label="Photo of a business team meeting around a white table, seen from above"></div>
  </section>

  <section class="panel panel--light">
    <div class="panel-body">
      <h2 class="section-title">Case Study</h2>
      <p class="copy"><strong>Client:</strong> name of the law firm, city and size.</p>
      <p class="case-label">Challenge</p>
      <p class="copy">Describe the problem the firm faced with in-house admin work.</p>
      <p class="case-label">Solution</p>
      <p class="copy">Describe the services we provided and how they were set up.</p>
      <p class="case-label">Results</p>
      <p class="copy">Summarise savings, speed and accuracy gained.</p>
      <svg class="chart" width="116" height="78" viewBox="0 0 116 78" role="img" aria-label="Bar chart of cost before and after">
        <line x1="0" y1="64" x2="116" y2="64" stroke="#2b2b2b" stroke-width="0.8"/>
        <rect x="18" y="8" width="28" height="56" fill="#666766"/>
        <rect x="70" y="30" width="28" height="34" fill="#84264f"/>
        <text x="32" y="74" font-size="7" text-anchor="middle" fill="#2b2b2b" font-family="Barlow, sans-serif">Before</text>
        <text x="84" y="74" font-size="7" text-anchor="middle" fill="#2b2b2b" font-family="Barlow, sans-serif">After</text>
      </svg>
      <p class="copy" style="margin-top:6px">“Insert a short client quote here.”</p>
    </div>
    <div class="photo photo--teamwork" role="img" aria-label="Photo of team members stacking their hands together"></div>
  </section>

  <section class="panel panel--grey">
    <div class="panel-body">
      <h2 class="section-title">Our Value</h2>
      <p class="copy">What law firms gain by working with us.</p>
      <ul class="value-list">
        <li><svg width="10" height="10" viewBox="0 0 10 10"><path d="M1 5l3 3 5-7" fill="none" stroke="#84264f" stroke-width="1.6"/></svg><span><strong>Countrywide coverage</strong>One partner for every tribunal in Brazil.</span></li>
        <li><svg width="10" height="10" viewBox="0 0 10 10"><path d="M1 5l3 3 5-7" fill="none" stroke="#84264f" stroke-width="1.6"/></svg><span><strong>Order and follow online</strong>Full visibility of every request.</span></li>
        <li><svg width="10" height="10" viewBox="0 0 10 10"><path d="M1 5l3 3 5-7" fill="none" stroke="#84264f" stroke-width="1.6"/></svg><span><strong>Agreed prices</strong>Pre-defined fees, no surprises.</span></li>
        <li><svg width="10" height="10" viewBox="0 0 10 10"><path d="M1 5l3 3 5-7" fill="none" stroke="#84264f" stroke-width="1.6"/></svg><span><strong>Timeliness and accuracy</strong>Guaranteed deadlines and quality.</span></li>
      </ul>
      <div class="contact">
        <strong>Get in touch</strong>
        Phone: +55 00 0000-0000<br>
        www.vtamplexo.com.br
      </div>
    </div>
    <div class="photo photo--review" role="img" aria-label="Photo of colleagues pointing pens at documents during a review"></div>
  </section>

</main>
</body>
</html>
```